Bref créative
Fjellbrinken Tannregulering Stationery
Orthodontic Clinic
Professional
Fjellbrinken Tannregulering
Kjeveortoped Stian Haugvik
Myrbakkvegen 128
Postboks 71 Kvernvika
5912 BERGEN
post@smilbrink.no
www.smilbrink.no
Telefon 55 83 17 62

```html
<!DOCTYPE html>
<html lang="no">
<head>
<meta charset="utf-8">
<title>Fjellbrinken Tannregulering – Visittkort</title>
<link rel="stylesheet" href="https://fonts.googleapis.com/css2?family=Roboto+Condensed:wght@400;700&family=Open+Sans:wght@400;600&display=swap">
<style>
  :root {
    --backdrop: #e9e4dc;
    --card: #ffffff;
    --brand-blue: #1d6fb5;
    --brand-green: #7cc242;
    --ink: #4a4a4a;
    --ink-soft: #7a7a7a;
  }
  * { margin: 0; padding: 0; box-sizing: border-box; }
  html, body {
    width: 1200px; height: 674px; overflow: hidden;
    background: var(--backdrop);
    font-family: "Open Sans", Arial, sans-serif;
  }
  .sheet { position: relative; width: 1200px; height: 674px; }
  .card {
    position: absolute; top: 192px;
    width: 480px; height: 290px;
    background: var(--card);
    border-radius: 22px;
    box-shadow: 0 6px 18px rgba(0,0,0,.18);
    overflow: hidden;
  }
  .card--front { left: 96px; }
  .card--back { left: 624px; }

  /* front: header */
  .header-strip { position: absolute; top: 22px; right: 0; text-align: right; }
  .header-strip__name {
    font-family: "Roboto Condensed", Arial, sans-serif;
    font-weight: 700; font-size: 17px; color: var(--brand-blue);
    padding-right: 20px;
  }
  .header-strip__rule {
    height: 5px; width: 250px; margin-left: auto; margin-top: 2px;
    background: var(--brand-green);
  }
  .header-strip__title {
    font-size: 10.5px; color: var(--brand-green); padding-right: 20px; margin-top: 2px;
  }

  /* front: identity */
  .identity { position: absolute; left: 26px; top: 88px; width: 360px; }
  .identity__row { display: flex; align-items: center; gap: 12px; }
  .identity__dot {
    width: 44px; height: 44px; border-radius: 50%;
    background: var(--brand-blue); flex: none;
  }
  .identity__name {
    font-family: "Roboto Condensed", Arial, sans-serif;
    font-weight: 700; font-size: 27px; line-height: 1.02;
    color: var(--brand-blue); text-transform: uppercase;
  }
  .identity__title {
    font-family: "Roboto Condensed", Arial, sans-serif;
    font-size: 17px; color: var(--brand-green);
    margin: 4px 0 0 56px;
  }
  .identity__rule {
    height: 2px; background: var(--brand-blue); margin: 6px 0 0 56px; width: 290px;
  }

  /* front: contact */
  .contact {
    position: absolute; left: 82px; top: 198px;
    font-size: 10.5px; line-height: 1.45; color: var(--ink);
  }
  .contact__label { color: var(--brand-green); font-weight: 600; }
  .contact__sep { color: var(--ink-soft); margin: 0 4px; }

  /* back */
  .back-mark {
    position: absolute; left: 40px; top: 96px;
    width: 96px; height: 96px; border-radius: 50%;
    background: var(--brand-blue);
  }
  .back-band {
    position: absolute; left: 166px; right: 0; top: 136px; height: 28px;
    background: var(--brand-green);
    display: flex; align-items: center; padding-left: 16px;
    font-family: "Roboto Condensed", Arial, sans-serif;
    font-weight: 700; font-size: 19px; color: #fff;
  }
  .back-name {
    position: absolute; left: 166px; top: 96px;
    font-family: "Roboto Condensed", Arial, sans-serif;
    font-weight: 700; font-size: 20px; color: var(--brand-blue);
    text-transform: uppercase;
  }
</style>
</head>
<body>
<main class="sheet">

  <section class="card card--front" aria-label="Visittkort forside">
    <header class="header-strip">
      <div class="header-strip__name">Fjellbrinken Tannregulering</div>
      <div class="header-strip__rule"></div>
      <div class="header-strip__title">Kjeveortoped Stian Haugvik</div>
    </header>

    <div class="identity">
      <div class="identity__row">
        <span class="identity__dot"></span>
        <div class="identity__name">Fjellbrinken<br>Tannregulering</div>
      </div>
      <div class="identity__title">Kjeveortoped Stian Haugvik</div>
      <div class="identity__rule"></div>
    </div>

    <address class="contact" style="font-style:normal">
      <div>Myrbakkvegen 128 Postboks 71 Kvernvika</div>
      <div>5912 BERGEN</div>
      <div><span class="contact__label">Ph :</span> 55 83 17 62<span class="contact__sep">|</span><span class="contact__label">Fax :</span> 55 40 92 18</div>
      <div><span class="contact__label">Email :</span> post@smilbrink.no</div>
      <div><span class="contact__label">Web :</span> www.smilbrink.no</div>
    </address>
  </section>

  <section class="card card--back" aria-label="Visittkort bakside">
    <span class="back-mark"></span>
    <div class="back-name">Fjellbrinken Tannregulering</div>
    <div class="back-band">www.smilbrink.no</div>
  </section>

</main>
</body>
</html>
```